Corporate Web Redesign Project - coded

We would like redesign/refresh of our current site that would allow us to increase the depth of content and create a high quality impression for visitors.

Current site - http://corvanisystems.com/

A previous web redesign project has improved our site but it has not really reached the level we require.

Our customers are global, blue chip, organisations and a professional, corporate style of site is required.

Please note we would prefer a coded website to a just a design. We are happy to provide a zip of our current site if required.
Updates

                                   

Target Market(s)

Global oil and gas producers, KR, Tamberline, Orvadex etc.

Industry/Entity Type

It Professional

Requirements
Must have
• Design should support the level of content we currently have in the existing sitemap - although it should be expandable a site design for a large / complex site would not be appropriate

All current content / pages to be reflected in design

Must be visually appealing

Intuitive and clear navigation that is expandable

Display a high level of professionalism

Use a consistent palette of colours that complements our logo

Clean and organized layout

A way to capture visitor’s information or Call to action (i.e. contact link or form) on every page

Prominent Contact Information
Should not have
• Flash

```html
<!DOCTYPE html>
<html lang="en">
<head>
<meta charset="utf-8">
<title>Corvani Systems</title>
<link href="https://fonts.googleapis.com/css2?family=Source+Sans+3:wght@400;600;700&display=swap" rel="stylesheet">
<style>
:root{
  --teal:#4a7a86;
  --teal-dark:#3d6874;
  --ink:#333;
  --muted:#555;
  --line:#d8d8d8;
  --footer:#0e0e0e;
  --white:#fff;
  --sky:#3f74a8;
  --sand:#c9b79b;
}
*{box-sizing:border-box;margin:0;padding:0}
html,body{width:981px;height:1200px;overflow:hidden;background:var(--white)}
body{font-family:"Source Sans 3",Arial,sans-serif;color:var(--ink);position:relative}
.abs{position:absolute}

/* header */
.brand{left:71px;top:40px;display:flex;align-items:center;gap:10px}
.brand-mark{width:34px;height:34px;border-radius:50%;background:var(--teal)}
.brand-name{font-size:26px;font-weight:700;color:var(--teal);letter-spacing:.5px}
.phone{left:553px;top:27px;display:flex;align-items:center;gap:10px;font-size:20px;color:#555}
.search{left:726px;top:25px;width:185px;height:28px;border:1px solid #c8c8c8;border-radius:3px;font-size:12px;font-style:italic;color:#999;padding:6px 8px}
.search svg{position:absolute;right:8px;top:7px}
.nav{left:470px;top:84px;display:flex;gap:36px;font-size:15.5px;color:#333}
.nav .current{color:var(--teal)}

/* hero */
.hero{left:71px;top:122px;width:839px;height:318px;background:linear-gradient(180deg,#3a70a8 0%,#7ca6cf 55%,#c9b79b 75%,#b7a387 100%)}
.slider-arrows{left:100px;top:409px;width:34px;height:23px;background:rgba(40,40,40,.75);border-radius:2px}
.quick-form{left:580px;top:165px;width:301px;height:245px;background:rgba(200,220,235,.35);border:1px solid rgba(255,255,255,.5)}
.quick-form h2{height:35px;background:linear-gradient(#555,#333);color:#fff;font-size:13.5px;font-weight:600;padding:10px 18px}
.field{position:absolute;background:#fff;border:1px solid #ddd;border-radius:2px;font-size:11.5px;color:#777;padding:6px 9px}
.send{position:absolute;left:208px;top:211px;width:72px;height:22px;background:var(--teal);color:#fff;font-size:11.5px;font-weight:600;text-align:center;line-height:22px;letter-spacing:.5px}

/* services */
.service{width:210px;text-align:center;top:466px}
.halo{width:120px;height:120px;border-radius:50%;margin:0 auto;background:radial-gradient(circle,#f4f4f4 60%,#e4e4e4 100%);display:flex;align-items:center;justify-content:center}
.disc{width:102px;height:102px;border-radius:50%;background:var(--teal);display:flex;align-items:center;justify-content:center}
.service h3{margin-top:6px;font-size:17.5px;font-weight:600;color:var(--teal);line-height:21px}
.service p{margin-top:4px;font-size:12.5px;line-height:18px;color:#333}

/* welcome */
.section-title{font-size:17px;color:var(--teal)}
.welcome-photo{left:72px;top:791px;width:179px;height:173px;border-radius:4px;background:linear-gradient(180deg,#5d87b0 0%,#2e5f8c 45%,#1d4870 100%)}
.lead{left:269px;top:786px;width:355px;font-size:14px;line-height:21px;color:var(--teal)}
.body-copy{left:269px;top:836px;width:355px;font-size:11.8px;line-height:20px;color:#444}
.news{left:668px;width:245px;display:flex;gap:12px}
.thumb{width:57px;height:48px;border:2px solid #eee;background:linear-gradient(135deg,#6b8b5a,#c9a57a);flex:none}
.news h4{font-size:12px;font-weight:700;color:#222}
.news p{font-size:12px;line-height:18px;color:#444}

/* partners */
.divider{left:71px;top:1003px;width:839px;height:12px;background:radial-gradient(ellipse at top,#e2e2e2 0%,rgba(255,255,255,0) 70%)}
.partners{left:71px;top:1044px;width:839px;display:flex;justify-content:space-between;align-items:center}
.partner{font-size:17px;font-weight:600;color:var(--teal-dark);display:flex;align-items:center;gap:6px}
.partner i{display:block;width:12px;height:12px;background:var(--teal-dark)}

/* footer */
.footer{left:0;top:1114px;width:981px;height:86px;background:var(--footer);color:#fff}
.footer-links{left:71px;top:18px;font-size:12px}
.copyright{left:71px;top:46px;font-size:11.5px}
.social{left:760px;top:28px;display:flex;gap:8px;font-size:11px;font-weight:600}
.social span{padding:5px 6px;border-radius:4px}
.s1{background:#1c9ad6}.s2{background:#c5241f}.s3{background:#0d6fb0}
</style>
</head>
<body>

<header>
  <div class="abs brand"><span class="brand-mark"></span><span class="brand-name">CORVANI SYSTEMS</span></div>
  <div class="abs phone">
    <svg width="21" height="21" viewBox="0 0 21 21"><circle cx="10.5" cy="10.5" r="10.5" fill="#8a8a8a"/><path d="M7 5.5l2 2-1 1.5c.7 1.5 1.8 2.6 3.3 3.3l1.5-1 2 2-1.3 1.7C10 15 6 11 5.5 6.8z" fill="#fff"/></svg>
    555-310-4872
  </div>
  <div class="abs search">Search..
    <svg width="12" height="12" viewBox="0 0 12 12"><circle cx="5" cy="5" r="3.8" fill="none" stroke="#999" stroke-width="1.6"/><path d="M8 8l3 3" stroke="#999" stroke-width="1.8"/></svg>
  </div>
  <nav class="abs nav"><span class="current">HOME</span><span>NEWS</span><span>ABOUT US</span><span>SOLUTIONS</span><span>CONTACT US</span></nav>
</header>

<section>
  <div class="abs hero" role="img" aria-label="Photograph of a red drilling rig truck in a desert oil field under blue sky"></div>
  <div class="abs slider-arrows">
    <svg width="34" height="23" viewBox="0 0 34 23"><path d="M12 7l-4 4.5 4 4.5M22 7l4 4.5-4 4.5" fill="none" stroke="#fff" stroke-width="1.4"/></svg>
  </div>
  <form class="abs quick-form">
    <h2>QUICK CONTACT FORM</h2>
    <div class="field" style="left:19px;top:52px;width:128px;height:28px">First Name</div>
    <div class="field" style="left:156px;top:52px;width:128px;height:28px">SecondName</div>
    <div class="field" style="left:19px;top:92px;width:128px;height:28px">Email</div>
    <div class="field" style="left:156px;top:92px;width:128px;height:28px">Company</div>
    <div class="field" style="left:19px;top:131px;width:265px;height:73px">Message</div>
    <div class="send">SEND</div>
  </form>
</section>

<section>
  <div class="abs service" style="left:57px">
    <div class="halo"><div class="disc"><svg width="60" height="60" viewBox="0 0 60 60"><circle cx="30" cy="30" r="25" fill="none" stroke="#fff" stroke-width="5"/><path d="M30 16v15h10" fill="none" stroke="#fff" stroke-width="5"/></svg></div></div>
    <h3>Time &amp;<br>Cost Estimation</h3>
    <p>Lorem ipsum dolor sit ameit<br>ing elit.Morbi ut elipsum tristiqu<br>umsan. Morbi ut elit utipsum tristi<br>Pellentesque habitant morb</p>
  </div>
  <div class="abs service" style="left:275px">
    <div class="halo"><div class="disc"><svg width="56" height="56" viewBox="0 0 56 56"><g fill="#fff"><circle cx="28" cy="28" r="17"/><g id="t"><rect x="23" y="4" width="10" height="12" rx="2"/><rect x="23" y="40" width="10" height="12" rx="2"/></g><use href="#t" transform="rotate(45 28 28)"/><use href="#t" transform="rotate(90 28 28)"/><use href="#t" transform="rotate(135 28 28)"/></g><circle cx="28" cy="28" r="7" fill="#4a7a86"/></svg></div></div>
    <h3>Materials &amp;<br>Cost Control</h3>
    <p>Lorem ipsum dolor sit amiet<br>ing elit.Morbi ut elipsum tristiqu<br>umsan. Morbi ut elit utipsum tristi<br>Pellentesque habitant morb</p>
  </div>
  <div class="abs service" style="left:498px">
    <div class="halo"><div class="disc"><svg width="56" height="56" viewBox="0 0 56 56"><g fill="none" stroke="#fff" stroke-width="3" stroke-linejoin="round"><path d="M16 14h14l2 30H18z"/><path d="M30 14l12-5v34l-10 6"/><path d="M10 24h10M10 31h10M10 38h10"/></g></svg></div></div>
    <h3>Lessons<br>Learned</h3>
    <p>Lorem ipsum dolor sit amiet<br>ing elit.Morbi ut elipsum tristiqu<br>umsan. Morbi ut elit utipsum tristi<br>Pellentesque habitant morb</p>
  </div>
  <div class="abs service" style="left:712px">
    <div class="halo"><div class="disc"><svg width="60" height="60" viewBox="0 0 60 60"><g fill="none" stroke="#fff" stroke-width="3" stroke-linejoin="round"><path d="M6 30L54 8 40 52 28 36z"/><path d="M54 8L28 36 26 50"/></g></svg></div></div>
    <h3>Services &amp;<br>Consulting</h3>
    <p>Lorem ipsum dolor sit amiet<br>ing elit.Morbi ut elipsum tristiqu<br>umsan. Morbi ut elit utipsum tristi<br>Pellentesque habitant morb</p>
  </div>
</section>

<section>
  <h2 class="abs section-title" style="left:71px;top:750px">Welcome to our website</h2>
  <div class="abs welcome-photo" role="img" aria-label="Photograph of an offshore oil drilling platform at sea"></div>
  <p class="abs lead">Ut wisi enim ad minim veniam, quis nostrud exerci tation ulli amcorper suscipit lobortis nisl ut aliquip exea.</p>
  <p class="abs body-copy">Incididunt ut labore et dolore magna aliqua. Ut enim ad minim veniam, quis nostrud exercitation ullamcolaboris nisi ut aliquip ex ea commodo consequat. Duis tefd aute iruredolor inreprehenderit in voluptate velit esse cillum.Dolore magna aliqua. Ut enim ad minim veniam, Quisnostru dexercitation ullamco laboris nisi ut aliquip. Ut enim ad minim veniam, quis nostrud exercitation ullamco laboris. Claritas est etiam processus dynamicus, qui sequitur mutationem.</p>

  <h2 class="abs section-title" style="left:668px;top:750px">Latest News</h2>
  <div class="abs news" style="top:785px"><div class="thumb" role="img" aria-label="Portrait photo for news item"></div><div><h4>During November 2013</h4><p>our Principal Petrophysicist, quisstr xercitation ullamco labors.</p></div></div>
  <div class="abs news" style="top:850px"><div class="thumb" role="img" aria-label="Portrait photo for news item"></div><div><h4>During November 2013</h4><p>At vero eois et accusamus et iustoid gnissimos ducimus qui.</p></div></div>
  <div class="abs news" style="top:915px"><div class="thumb" role="img" aria-label="Portrait photo for news item" style="background:linear-gradient(135deg,#d8d8d8,#9aa7b0)"></div><div><h4>During November 2013</h4><p>Deleniti atque corrupti quos doeset s molestias excepturi sint.</p></div></div>
</section>

<div class="abs divider"></div>
<div class="abs partners">
  <span class="partner">Halvern</span>
  <span class="partner">Aravel</span>
  <span class="partner"><i></i>KR</span>
  <span class="partner">Orvadex</span>
  <span class="partner">Enmera</span>
  <span class="partner">Westhollow</span>
  <span class="partner">Tolvar</span>
  <span class="partner">Brenmar</span>
</div>

<footer class="abs footer">
  <div class="abs footer-links">Home | News | About us | Solutions | Contact us</div>
  <div class="abs copyright">Copyrights 2013. All Rights Reserved.</div>
  <div class="abs social"><span class="s1">Chirpline</span><span class="s2">Viewcast</span><span class="s3">Linkwork</span></div>
</footer>

</body>
</html>
```